Curves, Cups and Commerce needs a book cover

I've been in lingerie business for 12 years, we own 5 x Lingerie stores. This is my story aimed at women in business or women who want to start a business. Essentially its a business book but also offers bra fitting advice. Although the book cover can be a bit cheeky it also needs to be tasteful. I do not have a colour in mind I just don't like it too girly. I like strong and bold with a feminine touch. The title needs to catch peoples attention when surrounded by so many other books. It needs to have some sort of image or texture. That could be a lace background texture. I like the idea of a bra hanging off the letters or some kind of image of a bra but a beautiful lacy bra. I would like the cover to be more beautiful than tacky even though it has the word 'boobs'.
Updates

Hi everyone, some great designs so far. Many of you have made a bra part of the 'Boobs' word. I thought this could work but it doesn't as it covers up the word 'Boobs' too much and I feel this word will catch peoples attention. If any of you would like to revise please feel free. thankyou Delia.

Target Market(s)

Women in business or women wanting to start a business.

Industry/Entity Type

Retail

Logo Text

Curves, Cups and Commerce

Font styles to use
Serif
Sans Serif

Colors

Designer to choose colors to be used in the design.

Requirements
Must have
• Title: Curves, Cups and Commerce (you could replace 'and' with '&' if it works better.
• Tagline: Elevating Lessons for Female Founders
• Author: Delia Forsgate
Nice to have
• An image of a bra, maybe in a playful way. It could hang off the letters or maybe the letters could look like a bra, but I'm concerned it may look tacky that way. Somehow incorporate a picture of a bra preferably as part of the title.
• I don't have images for you, you have the freedom to choose.
Should not have
• Although this book has boobs and bras in the title it must not be tacky or sexual. It is a business book.
• I do not like it to look too girly, probably not script unless its subtle.

```html
<!DOCTYPE html>
<html lang="en">
<head>
<meta charset="utf-8">
<title>Curves, Cups and Commerce — Delia Forsgate</title>
<link rel="stylesheet" href="https://fonts.googleapis.com/css2?family=Archivo:wght@700&family=Didact+Gothic&family=Indie+Flower&display=swap">
<style>
  :root {
    --paper: #ffffff;
    --ink: #0d0d0d;
    --lace-dark: #1c1c1c;
    --lace-mid: #3a3a3a;
    --lace-light: #6d6d6d;
    --tape: #4a4a4a;
  }
  html, body {
    margin: 0;
    padding: 0;
    overflow: hidden;
    background: var(--paper);
  }
  .cover {
    position: relative;
    width: 840px;
    height: 1200px;
    background: var(--paper);
    color: var(--ink);
    overflow: hidden;
  }
  .author {
    position: absolute;
    top: 36px;
    left: 0;
    width: 100%;
    margin: 0;
    text-align: center;
    font-family: "Archivo", Arial, sans-serif;
    font-weight: 700;
    font-size: 38px;
    line-height: 1.2;
  }
  .title {
    margin: 0;
    font-weight: normal;
  }
  .title-initial {
    position: absolute;
    left: 45px;
    top: 95px;
    width: 370px;
    height: 410px;
  }
  .title-line {
    position: absolute;
    display: block;
    font-family: "Didact Gothic", "Century Gothic", sans-serif;
    font-size: 124px;
    line-height: 1;
    white-space: nowrap;
  }
  .title-line--first { left: 408px; top: 352px; }
  .title-line--second { left: 262px; top: 545px; }
  .title-line--third {
    left: 232px;
    top: 735px;
    font-family: "Indie Flower", cursive;
    font-size: 106px;
  }
  .title-rule {
    position: absolute;
    left: 228px;
    top: 851px;
    width: 460px;
    height: 2px;
    background: var(--ink);
  }
  .tagline {
    position: absolute;
    bottom: 50px;
    left: 0;
    width: 100%;
    margin: 0;
    text-align: center;
    font-family: "Archivo", Arial, sans-serif;
    font-weight: 700;
    font-size: 35px;
    line-height: 1.2;
  }
</style>
</head>
<body>
  <main class="cover">
    <p class="author">Delia Forsgate</p>

    <h1 class="title" aria-label="Curves, Cups &amp; Commerce">
      <svg class="title-initial" viewBox="0 0 370 410" role="img" aria-label="Black lace bra and tape measure shaped into the letter C that opens the title">
        <defs>
          <radialGradient id="cup-tone" cx="45%" cy="45%" r="60%">
            <stop offset="0%" stop-color="var(--lace-light)"/>
            <stop offset="60%" stop-color="var(--lace-mid)"/>
            <stop offset="100%" stop-color="var(--lace-dark)"/>
          </radialGradient>
        </defs>
        <path class="tape-band" d="M0 240 L28 226 L200 372 L186 392 Z" fill="var(--tape)"/>
        <path class="initial-c" d="M345 129 A105 168 0 1 0 345 345 L307 313 A55 118 0 1 1 307 161 Z" fill="url(#cup-tone)"/>
      </svg>
      <span class="title-line title-line--first">urves</span>
      <span class="title-line title-line--second">Cups &amp;</span>
      <span class="title-line title-line--third">Commerce</span>
    </h1>
    <div class="title-rule"></div>

    <p class="tagline">Elevating Lessons for Female Founders</p>
  </main>
</body>
</html>
```